Texas Recycling and dump company needs Flyer design

We need a flyer design for a new company based in Austin Texas called 'Salvage Grove'. We receive dump materials on our property along with sell repurposed materials. We would like our design to include our logo along with add some creative designs to the flyer. Please use the attached image file as an outline. Blank boxes can be used for additional images.

Target Market(s)

Handing out flyers to new companies and hopefully getting contracts with them.

Font styles to use
Serif
Sans Serif

Requirements
Must have
• double sided
• images
Nice to have
• QR code with our website

```html
<!DOCTYPE html>
<html lang="en">
<head>
<meta charset="utf-8">
<title>Salvage Grove – We Collect</title>
<link href="https://fonts.googleapis.com/css2?family=Rubik:wght@500;700;800&display=swap" rel="stylesheet">
<style>
  :root {
    --paper: #e9eaec;
    --paper-light: #f3f4f5;
    --green: #7cc242;
    --blue: #1b75bb;
    --ink: #2b2b2b;
    --band: #262626;
    --yellow: #f7b92a;
    --red: #e5322d;
  }
  html, body {
    margin: 0;
    width: 1200px;
    height: 1200px;
    overflow: hidden;
    background: #ffffff;
  }
  .flyer {
    display: block;
    width: 1200px;
    height: 1200px;
    font-family: "Rubik", Arial, sans-serif;
  }
  .brand-name { fill: var(--blue); font-weight: 500; font-size: 21px; letter-spacing: 0.5px; }
  .headline { fill: var(--green); font-weight: 800; }
  .material-label { fill: var(--ink); font-weight: 700; font-size: 21px; }
  .hex-frame { fill: none; stroke: var(--green); stroke-width: 6; stroke-linejoin: round; }
  .slogan-band { fill: var(--band); }
  .slogan { fill: var(--yellow); font-weight: 700; font-size: 36px; }
  .contact-label { fill: var(--red); font-weight: 700; font-size: 21px; }
  .contact-value { fill: var(--ink); font-weight: 700; font-size: 21px; }
</style>
</head>
<body>
<svg class="flyer" viewBox="0 0 1200 1200" xmlns="http://www.w3.org/2000/svg">
  <defs>
    <radialGradient id="paperTone" cx="0.5" cy="0.45" r="0.75">
      <stop offset="0" stop-color="var(--paper-light)"/>
      <stop offset="1" stop-color="var(--paper)"/>
    </radialGradient>
    <linearGradient id="concreteTone" x1="0" y1="0" x2="0" y2="1">
      <stop offset="0" stop-color="#5e5e5e"/><stop offset="1" stop-color="#9a9a9a"/>
    </linearGradient>
    <linearGradient id="asphaltTone" x1="0" y1="0" x2="0" y2="1">
      <stop offset="0" stop-color="#cfe0e8"/><stop offset="0.45" stop-color="#e8dca0"/><stop offset="0.55" stop-color="#4a4a36"/><stop offset="1" stop-color="#8a8270"/>
    </linearGradient>
    <linearGradient id="soilTone" x1="0" y1="0" x2="0" y2="1">
      <stop offset="0" stop-color="#6b6a66"/><stop offset="1" stop-color="#3a322b"/>
    </linearGradient>
    <linearGradient id="debrisTone" x1="0" y1="0" x2="0" y2="1">
      <stop offset="0" stop-color="#c9ccd0"/><stop offset="0.45" stop-color="#b8bcc0"/><stop offset="0.55" stop-color="#5a4a3c"/><stop offset="1" stop-color="#3e342c"/>
    </linearGradient>
    <linearGradient id="woodTone" x1="0" y1="0" x2="1" y2="0">
      <stop offset="0" stop-color="#7a5a42"/><stop offset="1" stop-color="#c9a77a"/>
    </linearGradient>
  </defs>

  <!-- sheet -->
  <rect x="176" y="0" width="848" height="1200" fill="url(#paperTone)"/>

  <!-- brand -->
  <g class="brand">
    <circle cx="890" cy="118" r="26" fill="var(--green)"/>
    <text class="brand-name" x="890" y="166" text-anchor="middle">SALVAGE GROVE</text>
  </g>

  <!-- headline -->
  <text class="headline" x="654" y="238" font-size="72">We</text>
  <text class="headline" x="652" y="302" font-size="70">COLLECT</text>

  <!-- material hexagons -->
  <g class="materials">
    <polygon role="img" aria-label="Photo of stacked concrete blocks" fill="url(#concreteTone)" points="238,298 300,187 424,187 486,298 424,409 300,409"/>
    <polygon class="hex-frame" points="238,298 300,187 424,187 486,298 424,409 300,409"/>

    <polygon role="img" aria-label="Photo of an asphalt road at sunset" fill="url(#asphaltTone)" points="442,417 504,306 628,306 690,417 628,528 504,528"/>
    <polygon class="hex-frame" points="442,417 504,306 628,306 690,417 628,528 504,528"/>

    <polygon role="img" aria-label="Photo of a shovel in clean fill soil" fill="url(#soilTone)" points="238,538 300,427 424,427 486,538 424,649 300,649"/>
    <polygon class="hex-frame" points="238,538 300,427 424,427 486,538 424,649 300,649"/>

    <polygon role="img" aria-label="Photo of a pile of mixed debris" fill="url(#debrisTone)" points="442,660 504,549 628,549 690,660 628,771 504,771"/>
    <polygon class="hex-frame" points="442,660 504,549 628,549 690,660 628,771 504,771"/>

    <polygon role="img" aria-label="Photo of tree stumps and wood shavings" fill="url(#woodTone)" points="646,548 708,437 832,437 894,548 832,659 708,659"/>
    <polygon class="hex-frame" points="646,548 708,437 832,437 894,548 832,659 708,659"/>

    <text class="material-label" x="362" y="175" text-anchor="middle">Concrete</text>
    <text class="material-label" x="562" y="295" text-anchor="middle">Asphalt</text>
    <text class="material-label" x="358" y="677" text-anchor="middle">Clean fill</text>
    <text class="material-label" x="771" y="689" text-anchor="middle">Wood &amp; Brush</text>
  </g>

  <!-- slogan band -->
  <g class="slogan-block">
    <rect class="slogan-band" x="470" y="888" width="554" height="124"/>
    <text class="slogan" x="980" y="946" text-anchor="end">Cleaner the Product</text>
    <text class="slogan" x="980" y="985" text-anchor="end">Lower the Price</text>
  </g>

  <!-- contact -->
  <g class="contact">
    <text class="contact-label" x="234" y="1046">Address:</text>
    <text class="contact-value" x="234" y="1077">1820, Cedar Hollow Rd, Austin</text>
    <text class="contact-label" x="234" y="1108">Call:</text>
    <text class="contact-value" x="234" y="1139">512555 0148</text>
  </g>
</svg>
</body>
</html>
```